LABEL DESIGN NEEDED FOR Mabel Fernwood Cookies

I am starting a Cookie Company with my daughter Mabel that will begin by making chocolate chip cookies.
These labels will go on a 2.5 by 2x6 clear cellophane bag that we will use to give out samples of our cookies to others to introduce our new- company to them.
I want the label to be 2X3 for both the front and the back.
These labels are for a cookie business starting out by making chocolate chip cookies. We will start out using clear cellophane bags with gold twist ties.
The size of the bags we will be using at first are 2.5x2x6 and 3.5x2x7.5.
Again, the clear cellophane bags will contain chocolate chip cookies that are round and weigh 1.5 oz. each.
On the front of the label I want it to have my logo which says Mabel Fernwood Cookies (see attached) with the name of the cookie (Chocolate Chip) and the weight (3oz.)
On the back of the label I would like the following:
Ingredients: All-purpose Flour, Semisweet Chocolate Chips, Granulated Sugar, Light Brown Sugar, Butter, Egg yolk, Light Corn Syrup, Milk, Vanilla Extract, Baking Soda, Salt
We also need it to say:
These products were manufactured in a facility that processes nuts and other known allergens. i.e. Milk, Eggs, Wheat, Soy
and it needs to have my address:
Harlow Creek, Ohio 11942
I have attached three things which will help the artist:
1.Our company logo (Mabel Fernwood Cookies)
2.A front and back label of a packaging from a cookie company that I really liked and thought was very cute. This should give the artist a start in terms of what direction to head in.
Thank you so much for all your help and just let me know what I need to do next.

```html
<!DOCTYPE html>
<html lang="en">
<head>
<meta charset="utf-8">
<title>Mabel Fernwood Cookies – Chocolate Chip Sample Labels</title>
<link rel="stylesheet" href="https://fonts.googleapis.com/css2?family=Arimo:wght@400;700&family=Yellowtail&family=Playfair+Display:wght@400&display=swap">
<style>
  :root {
    --page: #f4f1ec;
    --white: #ffffff;
    --cocoa: #5e3614;
    --gold: #c5941c;
    --ink: #111111;
    --slate: #5b5b5b;
    --cut-line: #3a3a3a;
  }
  * { box-sizing: border-box; margin: 0; padding: 0; }
  html, body { width: 1200px; height: 1000px; overflow: hidden; }
  body {
    background: var(--page);
    position: relative;
    font-family: "Arimo", Arial, sans-serif;
    color: var(--ink);
  }
  .label { position: absolute; }
  .label svg.label-shape { position: absolute; inset: 0; filter: drop-shadow(3px 5px 5px rgba(0,0,0,.35)); }

  /* Front label */
  .label-front { left: 40px; top: 300px; width: 530px; height: 400px; }
  .brand-name {
    position: absolute; left: 0; right: 0; top: 92px;
    text-align: center;
    font-family: "Arimo", Arial, sans-serif;
    font-weight: 400; font-size: 26px; line-height: 1;
    color: var(--slate);
  }
  .flavour {
    position: absolute; left: 105px; width: 320px; top: 170px;
    text-align: center;
    font-family: "Yellowtail", cursive;
    font-weight: 400;
    color: var(--cocoa); font-size: 52px; line-height: 0.95;
  }
  .weight {
    position: absolute; left: 261px; top: 263px; width: 88px; height: 88px;
    display: flex; align-items: center; justify-content: center;
    font-family: "Playfair Display", serif; font-size: 26px; color: var(--slate);
  }

  /* Back label */
  .label-back { left: 630px; top: 320px; width: 540px; height: 370px; }
  .info-panel {
    position: absolute; left: 58px; top: 42px; width: 424px; height: 292px;
    padding: 26px 28px 20px 32px; font-size: 11px; line-height: 1.3;
  }
  .info-heading { font-weight: 700; }
  .ingredients, .allergens { text-align: justify; }
  .allergens { margin-top: 14px; }
  .used-by { margin-top: 16px; font-weight: 700; }
  .baked-block {
    position: absolute; left: 32px; top: 222px; width: 180px;
    border-top: 1px solid var(--ink); padding-top: 6px;
  }
  .recycle { position: absolute; left: 164px; top: 172px; width: 40px; height: 40px; }
</style>
</head>
<body>

<section class="label label-front" aria-label="Front label">
  <svg class="label-shape" width="530" height="400" viewBox="0 0 530 400">
    <defs>
      <clipPath id="front-cut">
        <path d="M0,0 L530,0 Q488,200 530,400 L0,400 Q42,200 0,0 Z"/>
      </clipPath>
    </defs>
    <g clip-path="url(#front-cut)" role="img" aria-label="Label backing with cream polka dots over white and gold bands">
      <rect x="0" y="0" width="530" height="185" fill="var(--white)"/>
      <rect x="0" y="185" width="530" height="60" fill="var(--cocoa)"/>
      <rect x="0" y="245" width="530" height="155" fill="var(--gold)"/>
    </g>
    <path d="M0,0 L530,0" stroke="var(--cut-line)" stroke-width="1.2" stroke-dasharray="5 4" fill="none"/>
    <rect class="name-card" x="105" y="145" width="320" height="140" rx="18" fill="var(--white)" stroke="var(--cocoa)" stroke-width="6"/>
    <circle cx="305" cy="307" r="44" fill="var(--white)"/>
  </svg>
  <p class="brand-name">Mabel Fernwood Cookies</p>
  <h1 class="flavour">Chocolate<br>Chip</h1>
  <div class="weight">3oz.</div>
</section>

<section class="label label-back" aria-label="Back label">
  <svg class="label-shape" width="540" height="370" viewBox="0 0 540 370">
    <defs>
      <clipPath id="back-cut">
        <path d="M0,0 L540,0 Q500,185 540,370 L0,370 Q40,185 0,0 Z"/>
      </clipPath>
    </defs>
    <g clip-path="url(#back-cut)" role="img" aria-label="Label backing with cream polka dots over white and gold bands">
      <rect x="0" y="0" width="540" height="230" fill="var(--white)"/>
      <rect x="0" y="230" width="540" height="140" fill="var(--gold)"/>
    </g>
    <path d="M0,0 L540,0" stroke="var(--cut-line)" stroke-width="1.2" stroke-dasharray="5 4" fill="none"/>
    <rect x="58" y="42" width="424" height="292" rx="12" fill="var(--white)"/>
  </svg>
  <div class="info-panel">
    <p class="info-heading">Ingredients:</p>
    <p class="ingredients">All-purpose Flour, Semisweet Chocolate Chips, Granulated Sugar, Light Brown Sugar, Butter, Egg yolk, Light Corn Syrup, Milk, Vanilla Extract, Baking Soda, Salt</p>
    <p class="allergens">These products were manufactured in a facility that processes nuts and other known allergens. i.e. Milk, Eggs, Wheat, Soy</p>
    <p class="used-by">Used By:</p>
    <svg class="recycle" viewBox="0 0 40 40" role="img" aria-label="Recyclable">
      <g fill="none" stroke="var(--ink)" stroke-width="4.5" stroke-linecap="butt">
        <path d="M12,16 L18,6 L22,6 L27,14"/>
        <path d="M30,21 L36,31 L33,35 L23,35"/>
        <path d="M16,35 L6,35 L4,31 L9,22"/>
      </g>
      <g fill="var(--ink)">
        <polygon points="22,16 32,16 30,8"/>
        <polygon points="24,29 24,40 17,35"/>
        <polygon points="4,21 13,19 13,27"/>
      </g>
    </svg>
    <div class="baked-block">
      <p class="info-heading">Baked at:</p>
      <p>Harlow Creek, Ohio 11942</p>
    </div>
  </div>
</section>

</body>
</html>
```